Im want a website LIKE KMT's and FleetStride.com's with product payment options like Wendaro's

I need a website LIKE KMT with a header made EXACTLY LIKE THAT OF FLEETSTRIDES .

The front page photo should be like that of FLEETSTRIDE's webpage as well.

The name of the website will be called "C.M. (Calmira Mesa)".

We will be targeting ALL MARKETS in a small town in central Panama and charging businesses "listing fees" like a phone book does but also providing informational blogs, news, and other interesting activities.

THIS IS A MULTI PAGE WEBSITE

THIS IS WHERE KMT's website meets Norvex/FleetStride.

Once the layout is built I will tweak and modify, add information, and upload items for sale.

Here is a list of specific categories that should be listed out above the front page header image/search bar

-- Home -- News -- Travel -- Activities -- Shop & Dine -- Store -- More... --

These categories should be spread across the bottom of the page in three sections:

WHATS SO GREAT ABOUT (Calmira Mesa),
HAND PICKED TOURS
ACTIVITIES etc.

Also lets use www.Wendaro.example 's
"HOT DESTINATIONS"
"BEAT THE BEST PRICES IN BOQUETE"
"OCTOBERS INSIDER PICKS"
"TOP DESTINATIONS"
and spread them in four sections side-by-side near the bottom of the page.

Overall I would like to see the finished product to be something LIKE KMT's and FleetStrides.

WE NEED ONLINE PAYMENT OPTIONS LIKE NORVEX'S WEBSITE HAS

This will be a desktop website but should be very mobile friendly as well.

-rodwell

P.S. Good luck!
Updates

If it isn't already too late to change the website name, the name of the website should be "Calmira Mesa". Added Friday, October 9, 2015

What do you guys think the budget should be to win this? Added Saturday, October 10, 2015

www.lunaverde.example is the most amazing simple site. Whoever can make me a replica with my specifications will win immediately!!!! Added Sunday, October 18, 2015

OMG www.lunaverde.example is the bomb!So simple and elegant. Whoever can make me an EXACT REPLICA OF WWW.LUNAVERDE.EXAMPLE as my site with the specifications mentioned in my brief will take home the $825.00 immediately! Good luck amigos! Added Sunday, October 18, 2015

Does anybody know how to add recurring monthly billing options on this website? Added Sunday, October 18, 2015

Target Market(s)

ALL MARKETS

Industry/Entity Type

Product

Coding

Coded - Design and coding required

Number of Pages Required

5+ page

Requirements
Must have
• Coinlark payment options.
• I must be able to add and remove photos/text and video from the HTML files in the page.
• Be creative my friends, and may the odds be forever in your favor!
Nice to have
• I added some photos of a good layout for our page below.

```html
<!DOCTYPE html>
<html lang="en">
<head>
<meta charset="utf-8">
<title>Calmira Mesa</title>
<link href="https://fonts.googleapis.com/css2?family=Open+Sans:wght@400;600;700&display=swap" rel="stylesheet">
<style>
:root{
  --teal:#1aa3b5;
  --teal-dark:#138797;
  --yellow:#f5c518;
  --ink:#333;
  --muted:#888;
  --line:#e3e3e3;
  --bg:#fff;
  --soft:#f4f4f4;
  --dark:#262626;
  --darker:#1b1b1b;
}
*{box-sizing:border-box;margin:0;padding:0}
html,body{width:1200px;height:3396px;overflow:hidden}
body{font-family:"Open Sans",Arial,sans-serif;color:var(--ink);background:var(--bg);font-size:13px;position:relative}
.wrap{width:1000px;margin:0 auto;position:relative}
.ph{display:block}

/* top bar */
.topbar{height:32px;background:#f2f2f2;border-bottom:1px solid var(--line);font-size:11px;color:#666}
.topbar .wrap{display:flex;align-items:center;height:32px;gap:24px}
.topbar .contact{display:flex;align-items:center;gap:6px}
.topbar .acct{margin-left:auto;display:flex;gap:14px}
.ico{width:12px;height:12px;fill:var(--teal)}

/* header */
.header{height:96px;background:#fff;border-bottom:1px solid var(--line)}
.header .wrap{display:flex;align-items:center;height:96px}
.logo{display:flex;align-items:center;gap:10px;font-size:28px;font-weight:600;color:var(--teal)}
.logo .dot{width:14px;height:14px;border-radius:50%;background:var(--teal)}
.nav{margin-left:auto;display:flex;height:96px}
.nav a{display:flex;align-items:center;padding:0 18px;font-size:12px;color:#555;text-decoration:none;border-left:1px solid var(--line)}
.nav a.active{color:var(--teal)}
.cart{width:72px;height:96px;background:var(--teal);color:#fff;display:flex;flex-direction:column;align-items:center;justify-content:center;font-size:11px;gap:6px}

/* hero */
.hero{height:692px;position:relative;background:linear-gradient(100deg,#4f6a2a 0%,#8aa04a 30%,#d9cf8a 55%,#7f8f3e 75%,#3f5622 100%)}
.hero-arrow{position:absolute;top:300px;width:24px;height:40px}
.hero-arrow.l{left:24px}.hero-arrow.r{right:24px}
.hero-list{position:absolute;left:140px;top:120px;display:flex;flex-direction:column;gap:14px}
.hero-list .tag{background:rgba(26,163,181,.92);color:#fff;font-size:26px;font-weight:600;padding:10px 22px;align-self:flex-start}
.hero-list .item{background:rgba(20,20,20,.55);color:#fff;font-size:20px;padding:10px 18px 10px 14px;display:flex;gap:12px;align-items:center;align-self:flex-start}
.hero-list .item svg{width:18px;height:18px}
.search{position:absolute;left:0;right:0;bottom:0;height:118px;background:rgba(19,135,151,.85);color:#fff}
.search .wrap{padding-top:16px}
.search h2{font-size:26px;font-weight:400}
.search p{font-size:11px;opacity:.85;margin:4px 0 10px}
.search-row{display:flex;align-items:center;gap:10px;font-size:12px}
.field{background:#fff;color:#777;height:26px;width:120px;padding:0 8px;display:flex;align-items:center;font-size:11px}
.field.sm{width:110px}
.btn-y{background:var(--yellow);color:#333;font-weight:600;height:26px;padding:0 28px;display:flex;align-items:center}

/* section titles */
.sec-title{display:flex;align-items:center;gap:22px;font-size:30px;font-weight:400;color:#444;justify-content:center}
.sec-title::before,.sec-title::after{content:"";height:1px;background:#cfcfcf;width:290px}

/* discover */
.discover{padding:36px 0 0;height:692px}
.disc-grid{display:grid;grid-template-columns:repeat(3,320px);gap:20px;margin-top:36px}
.tile{height:238px;position:relative;overflow:hidden}
.tile .cap{position:absolute;left:0;right:0;bottom:14px;text-align:center;color:#fff;font-size:14px;font-weight:600}
.tile.solid{background:var(--teal);color:#fff;display:flex;flex-direction:column;align-items:center;justify-content:center;text-align:center;padding:0 40px}
.tile.solid h3{font-size:16px;font-weight:600;margin-bottom:8px}
.tile.solid p{font-size:11px;line-height:1.5;opacity:.9}
.tile .ph{position:absolute;inset:0}

/* newsletter */
.newsletter{height:216px;background:linear-gradient(90deg,#2f3a44 0%,#4a5560 50%,#6e7267 80%,#4b5056 100%);color:#fff;text-align:center}
.newsletter h2{font-size:30px;font-weight:400;padding-top:40px}
.newsletter p{font-size:12px;opacity:.85;margin-top:6px}
.nl-row{display:flex;align-items:center;margin-top:30px;gap:20px}
.nl-row .field{width:340px;height:36px;font-size:12px}
.nl-row .field.zip{width:320px}
.nl-row .btn-y{margin-left:auto;width:172px;height:36px;justify-content:center;font-size:14px;font-weight:400}

/* top destinations */
.top-dest{padding:132px 0 0;height:912px}
.dest-grid{display:grid;grid-template-columns:repeat(3,316px);gap:36px 26px;margin-top:38px}
.card{border:1px solid var(--line);height:280px;position:relative}
.card .ph{height:214px}
.card .tag{position:absolute;left:12px;top:12px;background:#fff;color:#333;font-size:10px;font-weight:700;padding:3px 8px}
.card .foot{display:flex;align-items:center;justify-content:space-between;padding:0 14px;height:64px}
.card .foot h4{font-size:13px;font-weight:700;color:#444}
.btn-t{background:var(--teal);color:#fff;font-size:10px;font-weight:700;padding:7px 12px}

/* three columns */
.cols{height:300px;padding-top:20px}
.cols .wrap{display:grid;grid-template-columns:330px 330px 300px;gap:20px}
.col-h{display:flex;align-items:center;gap:8px;font-size:20px;color:#444;margin-bottom:18px}
.col-h .b{width:14px;height:14px;border-radius:50%;background:var(--teal)}
.hot{display:grid;grid-template-columns:1fr 1fr;gap:10px 16px}
.hot .row{display:flex;align-items:center;gap:10px;font-size:11px;font-weight:600;color:#555}
.hot .row .ph{width:52px;height:36px;flex:none}
.hot .row small{display:block;font-weight:400;color:var(--muted);font-size:10px}
.pick .ph{height:200px;position:relative}
.pick .cap{background:rgba(0,0,0,.6);color:#fff;font-size:12px;padding:8px 12px;margin-top:-34px;position:relative}
.quote{border:1px solid var(--line);background:#fff;padding:18px;font-size:11px;line-height:1.7;color:#666;height:200px;position:relative}
.quote .who{margin-top:10px;text-align:right;color:#444;font-weight:600}
.quote .stars{color:var(--muted);margin-top:6px}

/* social band */
.tweet-band{height:108px;background:var(--teal);color:#fff}
.tweet-band .wrap{display:flex;align-items:center;height:108px;gap:28px}
.tweet-band .mark{width:40px;height:40px;border-radius:50%;background:#fff;flex:none}
.tweet-band p{font-size:13px;line-height:1.6;max-width:760px}
.tweet-band .pager{margin-left:auto;display:flex;gap:6px}
.tweet-band .pager span{width:26px;height:22px;background:#fff;display:flex;align-items:center;justify-content:center}

/* footer */
.footer{height:272px;background:var(--dark);color:#bbb;padding-top:40px}
.footer .wrap{display:grid;grid-template-columns:230px 150px 150px 150px 240px;gap:20px}
.footer .flogo{font-size:24px;font-weight:600;color:var(--teal)}
.footer p{font-size:10px;line-height:1.6;margin-top:10px;color:#999}
.footer h5{font-size:11px;font-weight:700;color:#fff;margin-bottom:12px}
.footer ul{list-style:none;font-size:10px;line-height:2;color:#999}
.soc{display:flex;flex-direction:column;gap:6px}
.soc span{display:block;width:110px;height:18px;font-size:10px;color:#fff;padding-left:8px;line-height:18px}
.tw li{display:flex;gap:8px;line-height:1.5;margin-bottom:8px}
.tw li i{width:10px;height:10px;background:#777;border-radius:50%;flex:none;margin-top:3px}
.bottombar{height:76px;background:var(--darker);color:#888;font-size:10px}
.bottombar .wrap{display:flex;align-items:center;height:76px;gap:18px}
.bottombar .copy{margin-left:auto}
</style>
</head>
<body>

<div class="topbar">
  <div class="wrap">
    <span class="contact"><svg class="ico" viewBox="0 0 12 12"><rect x="0" y="2" width="12" height="8"/><path d="M0 2l6 5 6-5" stroke="#fff" fill="none"/></svg>hello@calmiramesa.example</span>
    <span class="contact"><svg class="ico" viewBox="0 0 12 12"><path d="M2 1h3l1 3-2 1c1 2 2 3 3 3l1-2 3 1v3c-6 1-10-4-9-9z"/></svg>+507 555 0142</span>
    <span class="acct"><span>Log in</span><span>Sign Up</span></span>
  </div>
</div>

<header class="header">
  <div class="wrap">
    <div class="logo"><span class="dot"></span>Calmira Mesa</div>
    <nav class="nav">
      <a class="active">Home</a><a>Store</a><a>News</a><a>Activities</a><a>Travel</a><a>Shop &amp; Dine</a><a>More</a><a>Contact</a>
    </nav>
    <div class="cart"><svg width="22" height="20" viewBox="0 0 22 20"><path d="M1 2h4l3 11h10l3-8H7" stroke="#fff" stroke-width="2" fill="none"/><circle cx="9" cy="17" r="1.8" fill="#fff"/><circle cx="17" cy="17" r="1.8" fill="#fff"/></svg>CART</div>
  </div>
</header>

<section class="hero" role="img" aria-label="Sunlit forest path with a backpacker standing on the right">
  <svg class="hero-arrow l" viewBox="0 0 24 40"><path d="M20 2L4 20l16 18" stroke="#fff" stroke-width="4" fill="none"/></svg>
  <svg class="hero-arrow r" viewBox="0 0 24 40"><path d="M4 2l16 18L4 38" stroke="#fff" stroke-width="4" fill="none"/></svg>
  <div class="hero-list">
    <div class="tag">Best For Travelling Website</div>
    <div class="item"><svg viewBox="0 0 18 18"><rect x="1" y="1" width="16" height="16" fill="none" stroke="#fff" stroke-width="2"/><path d="M4 9l3 3 7-7" stroke="#fff" stroke-width="2" fill="none"/></svg>Package Post Type</div>
    <div class="item"><svg viewBox="0 0 18 18"><rect x="1" y="1" width="16" height="16" fill="none" stroke="#fff" stroke-width="2"/><path d="M4 9l3 3 7-7" stroke="#fff" stroke-width="2" fill="none"/></svg>Booking Form by Quillpage Forms</div>
    <div class="item"><svg viewBox="0 0 18 18"><rect x="1" y="1" width="16" height="16" fill="none" stroke="#fff" stroke-width="2"/><path d="M4 9l3 3 7-7" stroke="#fff" stroke-width="2" fill="none"/></svg>Package Discount Feature</div>
    <div class="item"><svg viewBox="0 0 18 18"><rect x="1" y="1" width="16" height="16" fill="none" stroke="#fff" stroke-width="2"/><path d="M4 9l3 3 7-7" stroke="#fff" stroke-width="2" fill="none"/></svg>Pakcage Filtering System</div>
  </div>
  <div class="search">
    <div class="wrap">
      <h2>Search Travel on Calmira Mesa</h2>
      <p>Find tours, stays and local listings across the valley, compare prices and book your next trip in just a few easy steps with secure online payment.</p>
      <div class="search-row">
        <span>I want to Go from</span><span class="field">Select city</span><span class="field sm">Date</span>
        <span>to</span><span class="field">Select city</span><span class="field sm">Date</span>
        <span class="btn-y">Search</span>
      </div>
    </div>
  </div>
</section>

<section class="discover">
  <div class="wrap">
    <h2 class="sec-title">Discover Calmira Mesa</h2>
    <div class="disc-grid">
      <div class="tile solid"><h3>Best Maui Hotels</h3><p>Stay close to the beach, enjoy island views and find the perfect room at the best rate.</p></div>
      <div class="tile"><span class="ph" role="img" aria-label="Hotel room balcony overlooking the ocean" style="background:linear-gradient(160deg,#c9d9e4,#8fb1c9 50%,#d8c7a8)"></span><span class="cap">Harbor Crest Hotel Waikiki<br>Book Now</span></div>
      <div class="tile"><span class="ph" role="img" aria-label="Resort pool with palm trees" style="background:linear-gradient(160deg,#6fb3e0,#4aa0b8 50%,#2f7b4e)"></span><span class="cap">Big Island Best Value Hotels</span></div>
      <div class="tile"><span class="ph" role="img" aria-label="City beach skyline by the sea" style="background:linear-gradient(180deg,#8ec8ec,#5a9fc8 55%,#2d7ea6)"></span><span class="cap">Oahu Best Value Hotels</span></div>
      <div class="tile"><span class="ph" role="img" aria-label="Tropical resort with lagoon and palms" style="background:linear-gradient(180deg,#5aa9d6,#3e8f7a 50%,#2e6a3c)"></span><span class="cap">Maui Best Value Hotels</span></div>
      <div class="tile"><span class="ph" role="img" aria-label="Resort at dusk with purple sky" style="background:linear-gradient(180deg,#3a2b8c,#6a4fb0 50%,#1f5a8a)"></span><span class="cap">Kauai Best Value Hotels</span></div>
    </div>
  </div>
</section>

<section class="newsletter" role="img" aria-label="Couple overlooking a valley, darkened backdrop">
  <div class="wrap">
    <h2>Email Newsletter</h2>
    <p>Join our newsletter and get the latest and hottest local travel deals</p>
    <div class="nl-row"><span class="field">Your Email</span><span class="field zip">Zip Code</span><span class="btn-y">Subscribe</span></div>
  </div>
</section>

<section class="top-dest">
  <div class="wrap">
    <h2 class="sec-title">Top Destinations</h2>
    <div class="dest-grid">
      <div class="card"><span class="ph" role="img" aria-label="Mountain lake with green meadow" style="background:linear-gradient(180deg,#7db7e6,#8fa8b8 45%,#4f8a3a)"></span><span class="tag">MOUNTAINS</span><div class="foot"><h4>ALPS MOUNTAINS</h4><span class="btn-t">VIEW MORE</span></div></div>
      <div class="card"><span class="ph" role="img" aria-label="Coastal city with harbour" style="background:linear-gradient(180deg,#6aa8d8,#3f8bb0 50%,#3d7a4a)"></span><span class="tag">SEA TOURS</span><div class="foot"><h4>MONACO CITY</h4><span class="btn-t">VIEW MORE</span></div></div>
      <div class="card"><span class="ph" role="img" aria-label="Turquoise sea with palm island" style="background:linear-gradient(180deg,#9fd3ef,#3fb7c7 55%,#2a8f5a)"></span><span class="tag">SEA TOURS</span><div class="foot"><h4>MALDIVES</h4><span class="btn-t">VIEW MORE</span></div></div>
      <div class="card"><span class="ph" role="img" aria-label="Overwater bungalows in a lagoon" style="background:linear-gradient(180deg,#5ab0e0,#2fc0c8 55%,#1e9aa8)"></span><span class="tag">SEA TOURS</span><div class="foot"><h4>BORA BORA</h4><span class="btn-t">VIEW MORE</span></div></div>
      <div class="card"><span class="ph" role="img" aria-label="Green island hills above a blue bay" style="background:linear-gradient(180deg,#8cc6ea,#2f9f8a 50%,#2d6f3a)"></span><span class="tag">MOUNTAINS</span><div class="foot"><h4>CARPATHIAN MOUNTAINS</h4><span class="btn-t">VIEW MORE</span></div></div>
      <div class="card"><span class="ph" role="img" aria-label="Clear shallow water and white sand" style="background:linear-gradient(180deg,#aee0f5,#48c2d8 55%,#e8e0c4)"></span><span class="tag">CRUISE</span><div class="foot"><h4>MIAMI</h4><span class="btn-t">VIEW MORE</span></div></div>
    </div>
  </div>
</section>

<section class="cols">
  <div class="wrap">
    <div>
      <div class="col-h"><span class="b"></span>Hot Destinations</div>
      <div class="hot">
        <div class="row"><span class="ph" role="img" aria-label="Beach thumbnail" style="background:#5aa7cf"></span><span>MIAMI<small>From $599</small></span></div>
        <div class="row"><span class="ph" role="img" aria-label="Old town thumbnail" style="background:#c99a6a"></span><span>FLORENCE<small>From $649</small></span></div>
        <div class="row"><span class="ph" role="img" aria-label="Skyline thumbnail" style="background:#7a8fb0"></span><span>LAS VEGAS<small>From $399</small></span></div>
        <div class="row"><span class="ph" role="img" aria-label="Bridge thumbnail" style="background:#8aa3b5"></span><span>PARIS<small>From $799</small></span></div>
        <div class="row"><span class="ph" role="img" aria-label="Harbour thumbnail" style="background:#4f8fb8"></span><span>ROME<small>From $699</small></span></div>
        <div class="row"><span class="ph" role="img" aria-label="Coast thumbnail" style="background:#3fa0a8"></span><span>TURKEY<small>From $549</small></span></div>
        <div class="row"><span class="ph" role="img" aria-label="City thumbnail" style="background:#9a7f6a"></span><span>LONDON<small>From $759</small></span></div>
        <div class="row"><span class="ph" role="img" aria-label="Island thumbnail" style="background:#5cb08a"></span><span>HAWAII<small>From $899</small></span></div>
      </div>
    </div>
    <div class="pick">
      <div class="col-h"><span class="b"></span>October Insider's Pick</div>
      <span class="ph" role="img" aria-label="Mountain ruins under a cloudy sky" style="background:linear-gradient(180deg,#b9c6cf,#7f9a6a 55%,#4e6b3a)"></span>
      <div class="cap">Machu Picchu Peru: Top Rated Tours</div>
    </div>
    <div>
      <div class="col-h"><span class="b"></span>What Client Say</div>
      <div class="quote">
        "Booking our stay was quick and easy, the local guides were friendly and every tour matched the description. We found great places to eat and will be back next season for sure."
        <div class="stars">★ ★ ★ ★ ★</div>
        <div class="who">Lena Morales<br>Calmira Mesa</div>
      </div>
    </div>
  </div>
</section>

<section class="tweet-band">
  <div class="wrap">
    <span class="mark"></span>
    <p>@calmiramesa: "Working on the right thing is probably more important than working hard." — Local travel tips and weekly deals from the valley<br>2 days ago</p>
    <div class="pager"><span><svg width="8" height="10" viewBox="0 0 8 10"><path d="M6 1L2 5l4 4" stroke="#1aa3b5" stroke-width="2" fill="none"/></svg></span><span><svg width="8" height="10" viewBox="0 0 8 10"><path d="M2 1l4 4-4 4" stroke="#1aa3b5" stroke-width="2" fill="none"/></svg></span></div>
  </div>
</section>

<footer class="footer">
  <div class="wrap">
    <div><div class="flogo">Calmira Mesa</div><p>Local listings, tours, news and shops from our small mountain town, gathered in one friendly guide for visitors and neighbours alike.</p></div>
    <div><h5>FOLLOW US</h5><div class="soc"><span style="background:#3b5998">Friendbook</span><span style="background:#2fa8d8">Chirpline</span><span style="background:#d23f31">Share</span><span style="background:#555">Subscribe</span></div></div>
    <div><h5>BEST TOURS</h5><ul><li>Coffee Farm Tour</li><li>Volcano Hiking</li><li>River Rafting</li><li>Canopy Zipline</li><li>Hot Springs</li></ul></div>
    <div><h5>POPULAR COMPANIES</h5><ul><li>Mesa Lodge</li><li>Valley Cafe</li><li>Rio Outfitters</li><li>Cerro Tours</li><li>Town Market</li></ul></div>
    <div><h5>TWEETS</h5><ul class="tw"><li><i></i>New coffee tours open this weekend, book early.</li><li><i></i>Rainy season deals on lodges now live.</li><li><i></i>Market day every Saturday in the plaza.</li></ul></div>
  </div>
</footer>
<div class="bottombar">
  <div class="wrap"><span>PRIVACY POLICY</span><span>ABOUT US</span><span>SUPPORT</span><span>FAQ</span><span>BLOG</span><span>FORUM</span><span class="copy">Copyright © 2015 · All Rights Reserved</span></div>
</div>

</body>
</html>
```